Brochure for a conference with healthcare professionals

Creating a brochure with the information provided in the word document attached below.. along with the logo.. All the information for the brochure is in the word document.. I attached a logo of endocrinology dept in the files.. Use that logo more promintenly than the brenmore care logo..

Most of the designs submitted till now didn't understand what was written on the word document.. The tri-fold should be designed to tell a story.. it should capture the attention just by its title.. then all the information provided should hook them in..

Target Market(s)

Physicians and CEOs of hospitals

Industry/Entity Type

Healthcare

Font styles to use
Serif

Colors

Designer to choose colors to be used in the design.

Requirements
Must have
• Good and memorable design with pictures and elegant design.. The design I am expecting is a tri-fold 9x16 size that can be tested on quellorint.example..

```html
<!DOCTYPE html>
<html lang="en">
<head>
<meta charset="utf-8">
<title>Tele-Endocrinology Service Brochure</title>
<link href="https://fonts.googleapis.com/css2?family=Titillium+Web:ital,wght@1,700&family=Montserrat:wght@800&family=Quicksand:wght@500;700&display=swap" rel="stylesheet">
<style>
  :root{
    --bg:#d9d9db;
    --paper:#ffffff;
    --navy:#1f3c8f;
    --brand-green:#3a9a2a;
    --lime:#c4d633;
    --lime-deep:#9db52a;
    --orange:#f07d1a;
    --bubble:#2f7cc4;
    --cream:#f3f0df;
    --ink:#333333;
    --muted:#6b6b6b;
  }
  html,body{margin:0;padding:0;width:1200px;height:1200px;overflow:hidden;background:var(--bg);}
  .canvas{position:relative;width:1200px;height:1200px;}
  .front-panel{
    position:absolute;left:280px;top:70px;width:640px;height:1060px;
    background:var(--paper);overflow:hidden;
    box-shadow:0 10px 30px rgba(0,0,0,.15);
  }
  .panel-shapes{position:absolute;inset:0;}
  .brand{
    position:absolute;left:0;right:0;top:70px;
    display:flex;align-items:center;justify-content:center;gap:16px;
  }
  .brand-dot{width:46px;height:46px;border-radius:50%;background:var(--brand-green);}
  .brand-text{display:flex;flex-direction:column;}
  .brand-name{
    font-family:"Quicksand",sans-serif;font-weight:700;font-size:34px;line-height:1.05;color:var(--navy);
  }
  .brand-tagline{
    font-family:"Quicksand",sans-serif;font-weight:500;font-size:14px;color:var(--muted);margin-top:6px;
  }
  .benefit{
    position:absolute;display:flex;align-items:center;justify-content:center;text-align:center;
    font-family:"Titillium Web",sans-serif;font-style:italic;font-weight:700;
    color:#fff;text-transform:uppercase;line-height:1.05;
  }
  .service-title{
    position:absolute;left:30px;right:30px;top:842px;margin:0;
    font-family:"Montserrat",sans-serif;font-weight:800;font-size:27px;line-height:1.2;
    color:#fff;text-transform:uppercase;text-align:center;
  }
  .contact-strip{
    position:absolute;left:0;right:0;bottom:0;height:96px;background:var(--cream);
    display:flex;flex-direction:column;justify-content:center;padding:0 32px;box-sizing:border-box;
    font-family:"Quicksand",sans-serif;font-weight:500;font-size:15px;color:var(--ink);line-height:1.5;
  }
</style>
</head>
<body>
<div class="canvas">
  <section class="front-panel">
    <svg class="panel-shapes" width="640" height="1060" viewBox="0 0 640 1060">
      <defs>
        <linearGradient id="photoTone" x1="0" y1="0" x2="1" y2="0">
          <stop offset="0" stop-color="#ede3d6"/>
          <stop offset=".6" stop-color="#e4e2e0"/>
          <stop offset="1" stop-color="#6f8fb3"/>
        </linearGradient>
        <linearGradient id="limeTone" x1="0" y1="0" x2="0" y2="1">
          <stop offset="0" stop-color="var(--lime)"/>
          <stop offset="1" stop-color="var(--lime-deep)"/>
        </linearGradient>
      </defs>
      <rect class="lower-field" x="0" y="560" width="640" height="500" fill="url(#limeTone)"/>
      <path class="photo-area" role="img" aria-label="Photo of a doctor examining a young girl with a stethoscope"
            d="M0,300 Q320,200 640,270 L640,640 Q320,700 0,660 Z" fill="url(#photoTone)"/>
      <path d="M0,300 Q320,200 640,270" fill="none" stroke="var(--orange)" stroke-width="9"/>
      <path d="M0,660 Q320,700 640,640" fill="none" stroke="var(--orange)" stroke-width="9"/>
      <g class="benefit-bubbles" fill="var(--bubble)" stroke="#fff" stroke-width="4">
        <circle cx="330" cy="420" r="68"/>
        <circle cx="520" cy="548" r="96"/>
        <circle cx="190" cy="725" r="76"/>
        <circle cx="405" cy="725" r="94"/>
      </g>
    </svg>

    <header class="brand">
      <span class="brand-dot"></span>
      <div class="brand-text">
        <span class="brand-name">Northvale Endocrinology<br>and Obesity Medicine</span>
        <span class="brand-tagline">Compassionate care in a friendly environment</span>
      </div>
    </header>

    <div class="benefit" style="left:262px;top:352px;width:136px;height:136px;font-size:19px;">Achieve<br>weight loss</div>
    <div class="benefit" style="left:424px;top:452px;width:192px;height:192px;font-size:20px;">Decrease<br>wait-times for an<br>endocrinologist</div>
    <div class="benefit" style="left:114px;top:649px;width:152px;height:152px;font-size:26px;">Save on<br>commute</div>
    <div class="benefit" style="left:311px;top:631px;width:188px;height:188px;font-size:20px;">Control<br>diabetes and<br>thyroid<br>disorders</div>

    <h1 class="service-title">Tele-endocrinology service<br>by Northvale Endocrinology and<br>Obesity Medicine</h1>

    <footer class="contact-strip">
      <span>Northvale Endocrinology and Obesity Medicine, Riverton | Ph: 555-014-4848</span>
      <span>Brenmore Care | Ph: 1-800-555-0129 | Email: hello@brenmore-care.example</span>
    </footer>
  </section>
</div>
</body>
</html>
```